Buch-Cover für Berater, Coach und Trainer
Ich habe das erste Mal Ihre Leistung in Anspruch genommen und bin restlos zufrieden. Schön, wenn sich die Entscheidung für einen bestimmten Designer, auch hinterher als absolut richtig herausstellt. Es hätte nicht besser laufen können mit tv studio. Vielen Dank nochmals für die gute Kommunikation und Ihre professionellen Vorschläge.
Zielgruppe
Guten Tag,
ich bin Berater, Coach und Trainer und es geht um die Vermarktung meines (Sach-)Buches 'Deal Sprints'.
Titel des Buches:
Deal Sprints
Untertitel:
Das Upgrade für Ihre Verkaufskompetenz
Zielgruppe:
Verkäufer oder Menschen, die andere für ihre Ideen gewinnen möchten
Bitte melden Sie sich gerne bei Fragen.
Herzliche Grüße
Torsten Wehmeyer
Aufgabenstellung
Das das Buch recht modern geschrieben ist, sollte der Stil schon auch dem Inhalt entsprechen.
Der Titel muss kein Bild haben, gerne auch eine Illustration oder nur Text.
Als Dateiupload lege ich Ihnen den Klappentext bei.

```html
<!DOCTYPE html>
<html lang="de">
<head>
<meta charset="utf-8">
<title>Deal Sprints – Buchcover</title>
<link href="https://fonts.googleapis.com/css2?family=Montserrat:wght@700;800&display=swap" rel="stylesheet">
<style>
  :root {
    --cover-bg: #000000;
    --text-light: #ffffff;
    --accent-orange: #ff8a00;
    --strip-top: #ff3535;
    --strip-bottom: #ff9400;
  }
  html, body {
    margin: 0;
    padding: 0;
    overflow: hidden;
    background: var(--cover-bg);
  }
  .cover {
    position: relative;
    width: 752px;
    height: 1200px;
    background: var(--cover-bg);
    overflow: hidden;
    font-family: "Montserrat", Arial, sans-serif;
    color: var(--text-light);
  }
  .spine-strip {
    position: absolute;
    left: 0;
    top: 0;
    width: 70px;
    height: 1200px;
    background: linear-gradient(180deg, var(--strip-top) 0%, #ff5a28 30%, #ff7a14 60%, var(--strip-bottom) 100%);
  }
  .book-title {
    position: absolute;
    left: 70px;
    width: 682px;
    top: 154px;
    margin: 0;
    font-size: 78px;
    font-weight: 800;
    line-height: 1;
    letter-spacing: -0.5px;
    text-align: center;
    white-space: nowrap;
    text-transform: uppercase;
  }
  .cart-icon {
    position: absolute;
    left: 307px;
    top: 418px;
    width: 138px;
    height: 113px;
  }
  .book-subtitle {
    position: absolute;
    left: 96px;
    top: 665px;
    margin: 0;
    font-size: 48px;
    font-weight: 700;
    line-height: 50px;
    letter-spacing: -0.3px;
    text-transform: uppercase;
    white-space: nowrap;
  }
  .author-rule {
    position: absolute;
    left: 617px;
    top: 990px;
    width: 75px;
    height: 7px;
    background: var(--accent-orange);
  }
  .author-name {
    position: absolute;
    right: 54px;
    top: 1018px;
    margin: 0;
    font-size: 25px;
    font-weight: 700;
    line-height: 32px;
    letter-spacing: 2px;
    text-align: right;
    text-transform: uppercase;
  }
  .author-name .first-name {
    display: block;
    margin-right: 18px;
  }
  .author-name .last-name {
    display: block;
  }
</style>
</head>
<body>
  <main class="cover">
    <div class="spine-strip"></div>

    <h1 class="book-title">Deal Sprints</h1>

    <svg class="cart-icon" viewBox="0 0 138 113" aria-hidden="true">
      <g fill="none" stroke="var(--accent-orange)" stroke-width="8" stroke-linecap="round" stroke-linejoin="round">
        <path d="M4 4 H24 L44 70 H114 L134 20 H33"/>
        <circle cx="56" cy="95" r="12"/>
        <circle cx="105" cy="95" r="12"/>
      </g>
    </svg>

    <h2 class="book-subtitle">Das Upgrade für Ihre<br>Verkaufskompetenz</h2>

    <div class="author-rule"></div>
    <p class="author-name">
      <span class="first-name">Torsten</span>
      <span class="last-name">Wehmeyer</span>
    </p>
  </main>
</body>
</html>
```